Complete Banner Set For Web Display Ads - Including Zimbly

Ads are driving to a free web class on real estate investing made easy. The offer is for software and training that solves their number 1 challenge - Finding Deals.
Examples of copy suggestions and offer....
"Invest In Real Estate Like A Pro"
"Access Never Before Seen Inventory In Seconds"
"The Country's Best Source For Off-Market Deals"
Brody Halvaney "#1 Real Estate Investing Strategy"
Real Estate

```html
<!DOCTYPE html>
<html lang="en">
<head>
<meta charset="UTF-8">
<title>Invest In Real Estate Like A Pro</title>
<link href="https://fonts.googleapis.com/css2?family=Roboto:wght@400;700;900&display=swap" rel="stylesheet">
<style>
  :root {
    --orange: #f5871f;
    --green: #8cc63f;
    --plum: #7b4c5e;
    --ink: #2f2f2f;
    --white: #ffffff;
    --scene-warm: #d9c3a8;
    --scene-light: #f3ece4;
    --portrait-tone: #b9b1a8;
  }
  * { margin: 0; padding: 0; box-sizing: border-box; }
  html, body {
    width: 1200px;
    height: 998px;
    overflow: hidden;
    background: var(--white);
    font-family: "Roboto", Arial, sans-serif;
  }
  .banner {
    position: relative;
    width: 1200px;
    height: 998px;
    overflow: hidden;
    background: var(--white);
  }
  .backdrop {
    position: absolute;
    left: 0; top: 0;
    width: 1200px; height: 869px;
    background: linear-gradient(90deg, var(--scene-warm) 0%, var(--scene-light) 45%, var(--white) 72%);
  }
  .portrait {
    position: absolute;
    left: 110px; top: 0;
    width: 520px; height: 869px;
    background: linear-gradient(180deg, #cfc6bd 0%, var(--portrait-tone) 45%, #e6e2dc 100%);
    border-radius: 200px 200px 0 0;
  }
  .headline {
    position: absolute;
    left: 636px; top: 53px;
  }
  .headline-box {
    display: block;
    width: fit-content;
    color: var(--white);
    font-weight: 700;
    font-size: 84px;
    line-height: 1;
    letter-spacing: 1px;
    padding: 12px 22px 12px 20px;
    margin-bottom: 8px;
    text-transform: uppercase;
  }
  .headline-box.orange { background: var(--orange); }
  .headline-box.green { background: var(--green); }
  .benefits {
    position: absolute;
    left: 640px; top: 557px;
    list-style: none;
    width: 540px;
  }
  .benefits li {
    position: relative;
    padding-left: 36px;
    color: var(--ink);
    font-size: 36px;
    line-height: 48px;
    margin-bottom: 8px;
  }
  .benefits li::before {
    content: "";
    position: absolute;
    left: 6px; top: 19px;
    width: 12px; height: 12px;
    border-radius: 50%;
    background: var(--ink);
  }
  .footer-band {
    position: absolute;
    left: 0; top: 869px;
    width: 1200px; height: 129px;
    background: var(--plum);
  }
  .cta {
    position: absolute;
    left: 629px; top: 890px;
    width: 418px; height: 84px;
    border-radius: 42px;
    background: var(--orange);
    color: var(--white);
    font-weight: 700;
    font-size: 38px;
    letter-spacing: 1px;
    display: flex;
    align-items: center;
    justify-content: center;
    gap: 10px;
    text-decoration: none;
    text-transform: uppercase;
  }
  .cta svg { width: 26px; height: 26px; }
</style>
</head>
<body>
  <div class="banner">
    <div class="backdrop" role="img" aria-label="Softly blurred bright office interior"></div>
    <div class="portrait" role="img" aria-label="Portrait of the presenter in a light suit jacket and dark shirt"></div>

    <div class="headline">
      <span class="headline-box orange">Invest In</span>
      <span class="headline-box orange">Real Estate</span>
      <span class="headline-box green">Like A Pro</span>
    </div>

    <ul class="benefits">
      <li>Access Never Before Seen Inventory In Seconds</li>
      <li>The Country's Best Source For Off-Market Deals</li>
      <li>Brody Halvaney "#1 Real Estate Investing Strategy</li>
    </ul>

    <div class="footer-band"></div>
    <a class="cta" href="#">Get Started
      <svg viewBox="0 0 26 26" aria-hidden="true">
        <path d="M5 6 L12 13 L5 20 M13 6 L20 13 L13 20" fill="none" stroke="#ffffff" stroke-width="3.2" stroke-linecap="round" stroke-linejoin="round"/>
      </svg>
    </a>
  </div>
</body>
</html>
```